Corporate holiday e-card

We’re looking for a fun, energetic and personable winter holiday e-card design to send to our B2B customers. It should not reference a specific holiday; but it can refer to the ‘joys of the season’ or something similar, and also the ‘New Year.’ The design does not need to incorporate specific copy, but it could if integral to the design. Ideally the e-card would incorporate some aspects of the following:

- Our brand identity: elements from our company logo, such as the triad-plug graphic; images from our website; colors; etc.

-Winter themes such as snow, mountains, skiing, etc. are preferable.

-Tie-into our main market: software company providing resources for the renewable energy industry, primarily solar (for more information on the types of products we provide, see our website: www.brightvolta.example).

-We are open to the use of photographic or graphical images. We prefer a clean, modern, technology-oriented look/feel.

The card will be distributed via email, and as such, should be of appropriate size (both dimensionally and file-size).

Target Market(s)

B2B clean-energy

Industry/Entity Type

Software

Font styles to use
Sans Serif

Requirements
Must have
• -Incorporate elements of our brand identity (such as logo, colors, images, etc.)
-Appropriately formatted (dimensions & file size) for email distribution as an image.
Nice to have
• - Play off the winter theme, and incorporate an element of our main business area: solar energy.

```html
<!DOCTYPE html>
<html lang="en">
<head>
<meta charset="utf-8">
<title>Happy New Year 2014 – Holiday E-card</title>
<link rel="stylesheet" href="https://fonts.googleapis.com/css2?family=Dancing+Script:wght@700&display=swap">
<style>
  :root {
    --night-top: #202020;
    --night-mid: #3a3b3d;
    --night-edge: #151515;
    --snow: #ffffff;
    --flake-soft: rgba(255,255,255,0.85);
    --brand-blue: #3ba3dc;
    --tree-amber: #e8a21c;
    --tree-red: #e0462c;
    --tree-green: #1bab62;
    --tree-teal: #159b8c;
    --tree-blue: #4d9fd6;
    --tree-violet: #8a3fa8;
    --tree-grey: #2c2c2c;
  }
  html, body {
    margin: 0;
    padding: 0;
    overflow: hidden;
    background: var(--night-edge);
  }
  .ecard {
    position: relative;
    width: 1030px;
    height: 1200px;
    overflow: hidden;
    background: radial-gradient(ellipse at 50% 40%, var(--night-mid) 0%, var(--night-top) 60%, var(--night-edge) 100%);
  }
  .scene {
    position: absolute;
    inset: 0;
  }
  .greeting {
    position: absolute;
    left: 388px;
    top: 462px;
    margin: 0;
    font-family: "Dancing Script", cursive;
    font-weight: 700;
    font-size: 70px;
    line-height: 1;
    color: var(--snow);
    white-space: nowrap;
  }
  .brand {
    position: absolute;
    left: 30px;
    top: 1080px;
    display: flex;
    align-items: center;
    gap: 12px;
    font-family: "Dancing Script", cursive;
    font-weight: 700;
    font-size: 40px;
    color: var(--brand-blue);
  }
  .brand-dot {
    width: 26px;
    height: 26px;
    border-radius: 50%;
    background: var(--brand-blue);
  }
</style>
</head>
<body>
<main class="ecard">
  <svg class="scene" width="1030" height="1200" viewBox="0 0 1030 1200" xmlns="http://www.w3.org/2000/svg">
    <defs>
      <radialGradient id="flake-fill">
        <stop offset="0" stop-color="#ffffff" stop-opacity="0.9"/>
        <stop offset="0.6" stop-color="#ffffff" stop-opacity="0.45"/>
        <stop offset="1" stop-color="#ffffff" stop-opacity="0"/>
      </radialGradient>
      <linearGradient id="forest-fill" x1="0" x2="1" y1="0" y2="0">
        <stop offset="0" stop-color="var(--tree-amber)"/>
        <stop offset="0.12" stop-color="var(--tree-grey)"/>
        <stop offset="0.2" stop-color="var(--tree-blue)"/>
        <stop offset="0.35" stop-color="var(--tree-green)"/>
        <stop offset="0.45" stop-color="var(--tree-amber)"/>
        <stop offset="0.55" stop-color="var(--tree-red)"/>
        <stop offset="0.68" stop-color="var(--tree-red)"/>
        <stop offset="0.78" stop-color="var(--tree-green)"/>
        <stop offset="0.86" stop-color="var(--tree-violet)"/>
        <stop offset="0.93" stop-color="var(--tree-amber)"/>
        <stop offset="1" stop-color="var(--tree-teal)"/>
      </linearGradient>
    </defs>

    <g class="snowflakes" role="img" aria-label="Large white ornamental snowflakes falling across the night sky">
      <circle cx="145" cy="163" r="137" fill="url(#flake-fill)"/>
      <circle cx="405" cy="111" r="72" fill="url(#flake-fill)"/>
      <circle cx="609" cy="257" r="43" fill="url(#flake-fill)"/>
      <circle cx="397" cy="344" r="24" fill="url(#flake-fill)"/>
      <circle cx="859" cy="334" r="154" fill="url(#flake-fill)"/>
      <circle cx="180" cy="509" r="154" fill="url(#flake-fill)"/>
      <circle cx="642" cy="624" r="24" fill="url(#flake-fill)"/>
      <circle cx="428" cy="710" r="43" fill="url(#flake-fill)"/>
      <circle cx="635" cy="840" r="72" fill="url(#flake-fill)"/>
      <circle cx="898" cy="780" r="145" fill="url(#flake-fill)"/>
    </g>

    <rect class="forest" role="img" aria-label="Row of multicoloured speckled pine trees with a white deer standing among them"
          x="0" y="755" width="1030" height="330" fill="url(#forest-fill)" opacity="0.92"/>

    <path class="snow-ground" fill="var(--snow)"
          d="M0 1010 C 120 985, 220 990, 330 1010 C 480 1040, 620 1075, 780 1078 C 900 1080, 980 1070, 1030 1060 L 1030 1200 L 0 1200 Z"/>
  </svg>

  <h1 class="greeting">Happy New Year 2014</h1>

  <div class="brand">
    <span class="brand-dot"></span>
    <span class="brand-name">BrightVolta</span>
  </div>
</main>
</body>
</html>
```